Cloud Based Internet Protection Service Business Cards

I would like a professionally designed business card. I already have a logo which I have attached.

The business is an online cloud based internet protection service aimed parents, particularly at non-technical parents and also schools.

The card should be be quite simple in its design, not to full of text and give its information in a clear and concise manner

Target Market(s)

Parents (especially non-technical parents) and also schools

Industry/Entity Type

Internet

Colors

Designer to choose colors to be used in the design.

Requirements
Should not have
• Too much text or be too cluttered. No decorative fonts, just a clear and concise font.

```html
<!DOCTYPE html>
<html lang="en">
<head>
<meta charset="utf-8">
<title>Kinnow Shield – Business Card</title>
<link rel="stylesheet" href="https://fonts.googleapis.com/css2?family=Open+Sans:wght@400;600&display=swap">
<style>
  :root {
    --page: #ecebe8;
    --card: #ffffff;
    --blue: #2aa3c9;
    --blue-light: #4cc0dd;
    --blue-dark: #1c86aa;
    --ink: #3a3a3a;
    --swoosh: #d9dde0;
  }
  * { margin: 0; padding: 0; box-sizing: border-box; }
  html, body {
    width: 1200px; height: 1023px; overflow: hidden;
    background: var(--page);
    font-family: "Open Sans", Arial, sans-serif;
  }
  .stage {
    position: relative; width: 1200px; height: 1023px;
    display: flex; flex-direction: column; align-items: center; justify-content: center; gap: 60px;
  }
  .card {
    position: relative; width: 600px; height: 343px;
    border-radius: 4px; overflow: hidden;
    box-shadow: 0 10px 28px rgba(0,0,0,0.18);
  }
  .card-wave { position: absolute; inset: 0; width: 100%; height: 100%; }

  /* Front */
  .card-front { background: var(--card); }
  .front-brand {
    position: absolute; left: 40px; top: 48px;
    font-weight: 600; font-size: 34px; color: var(--blue-dark); letter-spacing: 0.5px;
    white-space: nowrap;
  }
  .front-address {
    position: absolute; left: 300px; top: 52px;
    display: flex; align-items: center; gap: 10px;
    font-size: 13px; color: var(--ink); letter-spacing: 0.4px;
    white-space: nowrap;
  }
  .person { position: absolute; left: 40px; top: 128px; }
  .person-name { font-size: 24px; font-weight: 600; color: var(--blue); line-height: 1.1; }
  .person-title { font-size: 14px; color: var(--ink); letter-spacing: 1.5px; margin-top: 4px; }
  .contact-list {
    position: absolute; left: 300px; top: 118px; list-style: none;
    font-size: 13px; color: var(--ink); letter-spacing: 0.4px;
  }
  .contact-list li { display: flex; align-items: center; gap: 10px; height: 22px; white-space: nowrap; }
  .icon { width: 14px; height: 14px; flex: none; }

  /* Back */
  .card-back { background: linear-gradient(120deg, var(--blue-light), var(--blue)); }
  .back-brand {
    position: absolute; left: 0; right: 0; top: 120px;
    display: flex; align-items: center; justify-content: center; gap: 14px;
    font-weight: 600; font-size: 44px; color: #ffffff; letter-spacing: 1px;
    white-space: nowrap;
  }
  .back-brand .dot { width: 18px; height: 18px; border-radius: 50%; background: #ffffff; }
</style>
</head>
<body>
<main class="stage">

  <section class="card card-front" aria-label="Card front">
    <svg class="card-wave" viewBox="0 0 600 343" preserveAspectRatio="none" aria-hidden="true">
      <path d="M0 300 C180 300 360 280 600 150 L600 343 L0 343 Z" fill="var(--swoosh)"/>
      <path d="M0 315 C200 318 390 300 600 175 L600 343 L0 343 Z" fill="var(--blue)"/>
      <path d="M0 330 C220 332 400 318 600 205" fill="none" stroke="#ffffff" stroke-width="2" opacity="0.6"/>
    </svg>

    <div class="front-brand">Kinnow Shield</div>

    <div class="front-address">
      <svg class="icon" viewBox="0 0 14 14" aria-hidden="true"><rect width="14" height="14" rx="2" fill="var(--blue)"/><path d="M7 3a2.5 2.5 0 0 0-2.5 2.5C4.5 8 7 11 7 11s2.5-3 2.5-5.5A2.5 2.5 0 0 0 7 3z" fill="#fff"/></svg>
      <span>42 Maple Row, Eastfield, Westbury</span>
    </div>

    <div class="person">
      <div class="person-name">Your Name</div>
      <div class="person-title">Your Title</div>
    </div>

    <ul class="contact-list">
      <li><svg class="icon" viewBox="0 0 14 14" aria-hidden="true"><rect width="14" height="14" rx="2" fill="var(--blue)"/><rect x="4" y="3" width="6" height="8" rx="1" fill="#fff"/></svg>0161 555 0142</li>
      <li><svg class="icon" viewBox="0 0 14 14" aria-hidden="true"><rect width="14" height="14" rx="2" fill="var(--blue)"/><path d="M4 4c0 4 2 6 6 6l1-2-2-1-1 1c-1-.5-2-1.5-2.5-2.5l1-1-1-2z" fill="#fff"/></svg>0161 555 0187</li>
      <li><svg class="icon" viewBox="0 0 14 14" aria-hidden="true"><rect width="14" height="14" rx="2" fill="var(--blue)"/><rect x="3" y="4" width="8" height="6" fill="#fff"/><path d="M3 4l4 3 4-3" fill="none" stroke="var(--blue)" stroke-width="1"/></svg>hello@kinnowshield.com</li>
      <li><svg class="icon" viewBox="0 0 14 14" aria-hidden="true"><rect width="14" height="14" rx="2" fill="var(--blue)"/><circle cx="7" cy="7" r="3.5" fill="none" stroke="#fff" stroke-width="1.2"/><path d="M3.5 7h7" stroke="#fff" stroke-width="1"/></svg>www.kinnowshield.com</li>
    </ul>
  </section>

  <section class="card card-back" aria-label="Card back">
    <svg class="card-wave" viewBox="0 0 600 343" preserveAspectRatio="none" aria-hidden="true">
      <path d="M0 0 L0 343 L90 343 C70 230 40 110 0 0 Z" fill="var(--swoosh)"/>
      <path d="M0 0 L0 343 L70 343 C55 230 30 110 0 0 Z" fill="#ffffff"/>
      <path d="M20 0 C60 110 90 230 108 343" fill="none" stroke="#ffffff" stroke-width="3" opacity="0.8"/>
    </svg>
    <div class="back-brand"><span class="dot"></span>Kinnow Shield</div>
  </section>

</main>
</body>
</html>
```